IT Consultancy Needs Daring Webpage (uncoded)

We are looking for a web page for a small IT firm, Fable Systems. We provide remote IT services, website development and IT consultancy. We are looking for a website that is a bit unique and will look both professional and cutting edge.

We are mainly targeting high cash flow small businesses.
Feel free to play with our yellow/blue theme. We where aiming for similar colours to movie posters i.e the Copper Horizon, http://lnk.vexomo.com/q3TzW. Think metallic, flashy and classy like a colourful Zumo.
Updates

We have a website but it is very poor and we would prefer if you did not use it for inspiration.

We quite like this design http://gallery.pixelorva.com/designs/web/?order=24&offset=24#/k7m9px2

The three cornerstones of our business are Consult, Support and E-Marketing

other designs are welcome as well (different from the the link above)

Target Market(s)

Small Businesses

Industry/Entity Type

Movie

Requirements
Must have
• Space for Home, Services, Contact and Blog menu bars.

Our logo is ok, you are welcome to adjust it a little to meet your needs.

While we appreciate most websites have a dense middle ground for navigation panels, we would like the most important buttons highlighted as well as a slightly interesting background for example, instead of a plain colour background, a slight hint of a pattern or image.
Should not have
• Should not have a banner.

```html
<!DOCTYPE html>
<html lang="en">
<head>
<meta charset="utf-8">
<title>Fable Systems – Remote IT Services</title>
<link rel="stylesheet" href="https://fonts.googleapis.com/css2?family=Arimo:wght@400;700&family=Gelasio:wght@400&display=swap">
<style>
  :root {
    --nav-red: #d8262a;
    --header-white: #ffffff;
    --tag-dark: #2b2b2b;
    --tag-blue: #1b5a8c;
    --page-blue-top: #3a6a90;
    --page-blue-bottom: #4c8dbf;
    --consult-top: #f0f0f0;
    --consult-bottom: #dedfe2;
    --support-top: #5f9bd0;
    --support-bottom: #4f97d9;
    --market-top: #e85556;
    --market-bottom: #c92428;
    --ink-dark: #3b3b3b;
    --ink-light: #ffffff;
    --btn-navy: #27506e;
    --btn-grey: #e6e6e6;
    --btn-grey-ink: #6b6b6b;
    --rule: #a9c8e2;
    --field: #f4f4f4;
    --field-ink: #666;
    --social-dot: #2a78b8;
  }
  * { margin: 0; padding: 0; box-sizing: border-box; }
  html, body { width: 1200px; height: 1178px; overflow: hidden; }
  body {
    position: relative;
    font-family: "Arimo", Arial, sans-serif;
    background: linear-gradient(180deg, var(--page-blue-top) 0%, var(--page-blue-bottom) 100%);
    color: var(--ink-light);
  }
  .abs { position: absolute; }

  /* Header */
  .header { left: 0; top: 0; width: 1200px; height: 217px; background: var(--header-white); }
  .header-photo { left: 0; top: 0; width: 440px; height: 217px;
    background: linear-gradient(90deg, #6f6a66 0%, #bdb7b0 55%, #ffffff 100%); }
  .nav-bar { left: 385px; top: 0; width: 815px; height: 76px; }
  .nav { left: 0; top: 22px; width: 1200px; font-family: "Gelasio", Georgia, serif; font-size: 21.5px; color: #fff; }
  .nav a { position: absolute; color: inherit; text-decoration: none; white-space: nowrap; }
  .nav .sep { position: absolute; top: 11px; width: 1px; height: 8px; background: #f6b5b5; }
  .brand { left: 1052px; top: 86px; font-family: "Gelasio", Georgia, serif; font-size: 40px; line-height: 48px; color: var(--tag-blue); }
  .tagline { left: 523px; top: 113px; font-size: 20.5px; line-height: 30px; }
  .tagline .lead { color: var(--tag-dark); }
  .tagline .sub { color: var(--tag-blue); }

  /* Service columns */
  .service { top: 217px; height: 445px; border-radius: 0 0 9px 9px; }
  .service h2 { position: absolute; top: 19px; font-family: "Gelasio", Georgia, serif; font-weight: 400; font-size: 22.5px; }
  .service .copy { position: absolute; top: 63px; width: 350px; font-size: 17px; line-height: 24px; }
  .service .copy p + p { margin-top: 24px; }
  .service-consult { left: 8px; width: 388px; background: linear-gradient(180deg, var(--consult-top), var(--consult-bottom)); color: var(--ink-dark); }
  .service-support { left: 404px; width: 388px; background: linear-gradient(180deg, var(--support-top), var(--support-bottom)); }
  .service-marketing { left: 802px; width: 387px; background: linear-gradient(180deg, var(--market-top), var(--market-bottom)); }
  .read-more { width: 128px; height: 45px; border-radius: 9px; display: flex; align-items: center; justify-content: center;
    font-family: "Gelasio", Georgia, serif; font-size: 21px; color: #fff; }
  .read-more-consult { left: 238px; top: 637px; background: linear-gradient(180deg, #f7bd24, #e99f00); }
  .read-more-support { left: 635px; top: 637px; background: linear-gradient(180deg, #3b6987, var(--btn-navy)); }
  .read-more-marketing { left: 1032px; top: 637px; background: var(--btn-grey); color: var(--btn-grey-ink); }

  /* Lower section */
  .section-title { font-size: 16px; letter-spacing: 0.3px; color: #fff; }
  .rule { height: 1px; background: var(--rule); }
  .quote { left: 37px; width: 318px; font-size: 17px; line-height: 21.6px; }
  .quote-by { width: 320px; left: 29px; text-align: right; font-size: 16.5px; }
  .dash { left: 34px; top: 910px; width: 316px; border-top: 1px dashed #dfe9f2; }
  .newsletter-box { left: 457px; top: 778px; width: 325px; height: 52px; background: #fff; border-radius: 14px;
    color: #111; font-size: 16px; }
  .newsletter-box .label { position: absolute; left: 22px; top: 16px; }
  .newsletter-box .submit { position: absolute; right: 18px; top: 16px; font-weight: 700; font-size: 15.5px; }
  .social { top: 932px; height: 40px; display: flex; align-items: center; gap: 12px; font-weight: 700; font-size: 17.5px; }
  .social .dot { width: 40px; height: 40px; border-radius: 50%; background: var(--social-dot); }
  .field { left: 902px; width: 264px; background: var(--field); color: var(--field-ink); font-size: 15.5px; padding: 7px 11px; }
  .form-submit { left: 1067px; top: 978px; width: 102px; height: 38px; border-radius: 8px; background: var(--btn-navy);
    display: flex; align-items: center; justify-content: center; font-size: 16px; letter-spacing: 0.3px; }

  /* Footer */
  .footer-links { left: 0; top: 1100px; width: 1210px; text-align: center; font-size: 14.5px; word-spacing: 2px; }
  .footer-links span { margin: 0 9px; }
  .copyright { left: 0; top: 1131px; width: 1210px; text-align: center; font-size: 14.5px; }
</style>
</head>
<body>
  <header class="abs header">
    <div class="abs header-photo" role="img" aria-label="Photo of three business colleagues reviewing papers at a laptop"></div>
    <svg class="abs nav-bar" width="815" height="76" viewBox="0 0 815 76" aria-hidden="true">
      <defs>
        <linearGradient id="navGrad" x1="0" y1="0" x2="0" y2="1">
          <stop offset="0" stop-color="#ef5150"/>
          <stop offset="1" stop-color="#d2262a"/>
        </linearGradient>
      </defs>
      <path d="M0 0 H815 V72 H32 Q12 72 10 52 Z" fill="url(#navGrad)"/>
      <path d="M32 72 H815" stroke="#b51d20" stroke-width="2"/>
    </svg>
    <nav class="abs nav">
      <a style="left:468px">Home</a>
      <span class="sep" style="left:551px"></span>
      <a style="left:572px">Services</a>
      <span class="sep" style="left:675px"></span>
      <a style="left:697px">Support</a>
      <span class="sep" style="left:797px"></span>
      <a style="left:821px">Blog</a>
      <span class="sep" style="left:888px"></span>
      <a style="left:910px">Contact Us</a>
    </nav>
    <div class="abs brand">Fable</div>
    <div class="abs tagline">
      <div class="lead">REMOTE IT SERVICES</div>
      <div class="sub">WEBSITE DEVELOPMENT AND IT CONSULTANCY.</div>
    </div>
  </header>

  <section class="abs service service-consult">
    <h2 style="left:28px">Consult</h2>
    <div class="copy" style="left:28px">
      <p>Lorem Ipsum is simply dummy text of the printing and typesetting industry. Lorem Ipsum has been the industry's standard dummy text ever since the 1500s, when an unknown printer took a galley of type and scrambled it to make a type specimen book.</p>
      <p>Lorem Ipsum is simply dummy text of the printing and typesetting industry.</p>
      <p>Lorem Ipsum is simply dummy text of the printing and typesetting industry. Lorem Ipsum is simply dummy text of the printing and type-setting industry.</p>
    </div>
  </section>
  <section class="abs service service-support">
    <h2 style="left:16px">Support</h2>
    <div class="copy" style="left:26px">
      <p>Lorem Ipsum is simply dummy text of the printing and typesetting industry. Lorem Ipsum has been the industry's standard dummy text ever since the 1500s, when an unknown printer took a galley of type and scrambled it to make a type specimen book.</p>
      <p>Lorem Ipsum is simply dummy text of the printing and typesetting industry.</p>
      <p>Lorem Ipsum is simply dummy text of the printing and typesetting industry. Lorem Ipsum is simply dummy text of the printing and type-setting industry.</p>
    </div>
  </section>
  <section class="abs service service-marketing">
    <h2 style="left:23px">E-Marketing</h2>
    <div class="copy" style="left:25px">
      <p>Lorem Ipsum is simply dummy text of the printing and typesetting industry. Lorem Ipsum has been the industry's standard dummy text ever since the 1500s, when an unknown printer took a galley of type and scrambled it to make a type specimen book.</p>
      <p>Lorem Ipsum is simply dummy text of the printing and typesetting industry.</p>
      <p>Lorem Ipsum is simply dummy text of the printing and typesetting industry. Lorem Ipsum is simply dummy text of the printing and type-setting industry.</p>
    </div>
  </section>
  <a class="abs read-more read-more-consult">Read More</a>
  <a class="abs read-more read-more-support">Read More</a>
  <a class="abs read-more read-more-marketing">Read More</a>

  <div class="abs section-title" style="left:29px; top:717px">TESTIMONIALS</div>
  <div class="abs rule" style="left:29px; top:750px; width:334px"></div>
  <p class="abs quote" style="top:774px">Lorem Ipsum is simply dummy text of the printing and typesetting industry. Lorem Ipsum has been the industry's standard dummy text ever since the 1500s.</p>
  <div class="abs quote-by" style="top:875px">Ras, NEWYORK</div>
  <div class="abs dash"></div>
  <p class="abs quote" style="top:930px">Lorem Ipsum is simply dummy text of the printing and typesetting industry. Lorem Ipsum has been the industry's standard dummy text ever since the 1500s.</p>
  <div class="abs quote-by" style="top:1031px">Gen, NEWYORK</div>

  <div class="abs section-title" style="left:456px; top:716px">NEWSLETTER</div>
  <div class="abs rule" style="left:457px; top:750px; width:335px"></div>
  <div class="abs newsletter-box"><span class="label">Email</span><span class="submit">Submit &gt;&gt;</span></div>
  <div class="abs section-title" style="left:457px; top:877px">FOLLOW US ON</div>
  <div class="abs rule" style="left:457px; top:910px; width:335px"></div>
  <div class="abs social" style="left:460px"><span class="dot"></span>Friendlane</div>
  <div class="abs social" style="left:610px"><span class="dot"></span>Chirpwave</div>

  <div class="abs field" style="top:739px; height:34px">Name</div>
  <div class="abs field" style="top:782px; height:34px">Phone Number</div>
  <div class="abs field" style="top:826px; height:33px">Email Address</div>
  <div class="abs field" style="top:869px; height:97px">Comments</div>
  <div class="abs form-submit">SUBMIT</div>

  <div class="abs rule" style="left:34px; top:1074px; width:1124px"></div>
  <div class="abs footer-links">Home<span>|</span>Services<span>|</span>Support<span>|</span>Blog<span>|</span>Contact Us</div>
  <div class="abs copyright">Copyright © 2011 Fable</div>
</body>
</html>
```